Hearth Table Cover Design

Open to creative ideas, we don't have a set cover style in mind so have fun with it!
Front Cover for Ebook-Quorvex and vantor shelf. Book title is "Hearth Table" sub title is "A Gentle Map for Kitchen Rhythms", Author is Corinne L Waddell. Website is www.theolwynkitchenworks.com.
Open to creative ideas, we dont' have a set cover style in mind so have fun with it!
We have attached some pictures of Corinne which could be incorporated into the title. We can send you high def files if you need.
We have attached two book covers which we like to get you started, but feel free to have fun, we're looking for something creative and catchy

```html
<!DOCTYPE html>
<html lang="en">
<head>
<meta charset="utf-8">
<title>Hearth Table — Cover</title>
<link href="https://fonts.googleapis.com/css2?family=Archivo+Black&family=Yellowtail&family=Arimo:wght@400&display=swap" rel="stylesheet">
<style>
  :root {
    --paper: #ffffff;
    --ink: #1a1a1a;
    --title-green: #2f8a3c;
    --title-glow: #c9d94a;
    --band: #c3d553;
    --arc-deep: #7fb63c;
    --arc-light: #e4ef9c;
    --tile-blue: #cfe6f3;
    --tile-green: #e3efb8;
    --produce-green: #6fa83a;
    --produce-red: #d8402a;
    --fork-steel: #b9bec3;
  }
  html, body {
    margin: 0;
    padding: 0;
    overflow: hidden;
    background: var(--paper);
  }
  .cover {
    position: relative;
    width: 776px;
    height: 1200px;
    overflow: hidden;
    background: var(--paper);
  }
  .top-arc {
    position: absolute;
    inset: 0;
  }
  .tile-pattern {
    position: absolute;
    left: 440px;
    top: 70px;
    width: 336px;
    height: 460px;
    background:
      radial-gradient(ellipse at 60% 40%, var(--tile-blue) 0%, rgba(207,230,243,0.5) 40%, rgba(255,255,255,0) 72%),
      radial-gradient(ellipse at 30% 20%, var(--tile-green) 0%, rgba(255,255,255,0) 55%);
    opacity: 0.9;
  }
  .subtitle-band {
    position: absolute;
    left: 0;
    top: 998px;
    width: 776px;
    height: 142px;
    background: var(--band);
  }
  .subtitle {
    position: absolute;
    left: 196px;
    top: 1006px;
    width: 600px;
    margin: 0;
    font-family: "Arimo", Arial, sans-serif;
    font-weight: 400;
    font-size: 47px;
    line-height: 62px;
    color: var(--ink);
    text-align: center;
  }
  .produce-fork {
    position: absolute;
    left: 58px;
    top: 0;
    width: 190px;
    height: 1200px;
    border-radius: 0 0 40px 40px;
    background: linear-gradient(180deg,
      var(--produce-green) 0%,
      var(--produce-red) 16%,
      var(--produce-green) 30%,
      #c9a0b8 40%,
      var(--produce-red) 50%,
      var(--produce-green) 58%,
      var(--fork-steel) 62%,
      var(--fork-steel) 100%);
  }
  .author {
    position: absolute;
    left: 298px;
    top: 470px;
    margin: 0;
    font-family: "Archivo Black", "Arial Black", sans-serif;
    font-size: 41px;
    line-height: 1;
    color: var(--ink);
    letter-spacing: 0.5px;
  }
  .title {
    position: absolute;
    left: 330px;
    top: 560px;
    width: 420px;
    margin: 0;
    font-family: "Yellowtail", cursive;
    font-weight: 400;
    font-size: 132px;
    line-height: 140px;
    color: var(--title-green);
    text-align: center;
    text-shadow: 5px 5px 0 var(--title-glow);
  }
  .title span { display: block; }
</style>
</head>
<body>
  <main class="cover">
    <svg class="top-arc" width="776" height="1200" viewBox="0 0 776 1200" aria-hidden="true">
      <defs>
        <linearGradient id="arcFill" x1="0" y1="1" x2="1" y2="0">
          <stop offset="0" stop-color="var(--arc-light)"/>
          <stop offset="1" stop-color="var(--arc-deep)"/>
        </linearGradient>
      </defs>
      <circle cx="560" cy="-330" r="410" fill="url(#arcFill)"/>
    </svg>

    <div class="tile-pattern" role="img" aria-label="Soft pattern of blurred pale blue and green squares"></div>

    <div class="subtitle-band"></div>
    <p class="subtitle">A Gentle Map for<br>Kitchen Rhythms</p>

    <div class="produce-fork" role="img" aria-label="Photograph of a fork stacked with salad, cucumber, tomato, onion and olives"></div>

    <p class="author">Corinne L Waddell</p>
    <h1 class="title"><span>Hearth</span><span>Table</span></h1>
  </main>
</body>
</html>
```